VarloNet Link Systems Website Design

We are an Australian based telecommunications company who specialise in the design, build and implementation of mission critical communications infrastructure. We have offices throughout Australia, New Zealand and Europe. Our Customers are operators in multiple markets from Oil & Gas, Mining, Government, Utilities, Carrier & Transportation.

We also work with large multi-national companies, that provide telecommunication and services such as; Brevik, Haldorsen, Quorva, Tamarind and many more. We want to be able to achieve the same level of impressions and professionalism as what these companies present on their websites.

To reflect our recent move into the European market, we need our new site to reflect who we are as a company, and exhibit the fact we are not just based in Australia, but we are a global organisation. We want to have a fresh clean look, thats modern, dynamic and simple. Flat textures and colours are perfect for us to adapt to. A site that is based around content management, with a responsive design that can be used on all devices.

We have started to develop a basic design language that we would like to incorporate in our overall website design. We have attached some documents that highlight our design language and we can provide colour codes and fonts to ensure consistency.

Our existing site is: www.varlonetls.example. Please feel free to view and pick apart items. From this example, we would massive improvement in how the site looks, feels and functions. We also want social media to form a big part of our site, with the likes of posts from chirpwave and blogs posting capabilities.

If you require anymore information about VarloNet or our requirements, please do not hesitate to contact.

Thanks and good luck!

Target Market(s)

Potential & Existing Customers, New international customers & markets, New Market Sectors, Partners, Service Providers

Industry/Entity Type

Telecommunications

Coding

Coded - Design and coding required

Number of Pages Required

5+ page

Font styles to use
Sans Serif

Requirements
Must have
• Content Management, Responsive Design for multiple device compatibility, Social media integration, use of lots of imagery, drop down menus, search capabilities
Should not have
• No flash.

```html
<!DOCTYPE html>
<html lang="en">
<head>
<meta charset="utf-8">
<title>VarloNet Link Systems</title>
<link rel="stylesheet" href="https://fonts.googleapis.com/css2?family=Open+Sans:wght@400;600;700&family=Roboto+Condensed:wght@300;400;700&display=swap">
<style>
:root{
  --navy:#1f3566;
  --navy-deep:#1b2d58;
  --accent:#8b80c6;
  --ring:#dcdcea;
  --text:#555;
  --heading:#444;
  --grey-bg:#efefef;
  --field:#f1f1f1;
  --field-line:#cfcfcf;
  --white:#fff;
}
*{margin:0;padding:0;box-sizing:border-box}
html,body{width:1200px;height:3462px;overflow:hidden;background:var(--white)}
body{position:relative;font-family:"Open Sans",Arial,sans-serif;color:var(--text)}
.abs{position:absolute}
.cond{font-family:"Roboto Condensed","Arial Narrow",sans-serif}
.hl{color:var(--navy)}

/* hero */
.hero{left:0;top:0;width:1200px;height:803px;background:radial-gradient(ellipse at 70% 60%,#eaf4ff 0%,#9cc7ee 35%,#3f82c6 70%,#1e4f93 100%)}
.header{left:0;top:0;width:1200px;height:135px;background:linear-gradient(#ffffff 0%,rgba(255,255,255,.85) 70%,rgba(255,255,255,0) 100%)}
.brand{left:76px;top:48px;display:flex;align-items:center;gap:12px;font-family:"Roboto Condensed",sans-serif;font-weight:700;font-size:40px;color:var(--navy)}
.brand-dot{width:22px;height:22px;border-radius:50%;background:var(--accent)}
.search{left:655px;top:18px;width:240px;height:38px;border:1px solid #c9c9c9;background:#fff;font-size:15px;color:#777;padding:8px 10px}
.search svg{position:absolute;right:10px;top:9px}
.phone-top{left:946px;top:22px;display:flex;align-items:center;gap:10px;font-size:19px;font-weight:600;color:var(--navy)}
.nav{left:376px;top:64px;display:flex;height:47px;font-family:"Roboto Condensed",sans-serif;font-size:17px;text-transform:uppercase;color:#444}
.nav a{display:block;padding:0 21px;line-height:47px;text-decoration:none;color:inherit}
.nav a.active{background:var(--navy);color:#fff}
.hero-title{left:0;top:338px;width:1200px;text-align:center;font-family:"Roboto Condensed",sans-serif;font-size:38px;line-height:53px;color:#0c1c3c}
.btn{display:block;background:var(--navy);color:#fff;text-align:center;font-family:"Roboto Condensed",sans-serif;text-transform:uppercase;border-radius:30px;text-decoration:none}
.hero-btn{left:496px;top:468px;width:208px;height:60px;line-height:60px;font-size:22px;font-weight:700}

/* welcome */
.welcome-title{left:0;top:852px;width:1200px;text-align:center;font-family:"Roboto Condensed",sans-serif;font-size:46px;color:var(--heading)}
.welcome-copy{left:150px;top:920px;width:900px;text-align:center;font-size:15.5px;line-height:25px}
.feature-img{width:210px;height:138px}
.feature-title{font-family:"Roboto Condensed",sans-serif;font-size:28px;color:var(--heading)}
.feature-copy{font-size:14.5px;line-height:24px;width:285px;margin-top:8px}
.more{font-size:14px;font-weight:700;color:var(--navy);margin-top:10px;display:flex;gap:6px;align-items:center}

/* business */
.business{left:0;top:1292px;width:1200px;height:496px;background:var(--grey-bg)}
.section-title{width:1200px;left:0;text-align:center;font-family:"Roboto Condensed",sans-serif;font-size:46px;color:var(--heading)}
.service{width:200px;text-align:center}
.service svg{display:block;margin:0 auto}
.service h3{font-family:"Roboto Condensed",sans-serif;font-weight:400;font-size:21px;line-height:27px;color:var(--navy);margin-top:22px}
.service p{font-size:13.5px;line-height:25px;margin-top:6px}

/* sectors */
.sectors{left:0;top:1788px;width:1200px;height:427px;background:linear-gradient(100deg,#2a4f8e 0%,#1e3f7a 50%,#27528f 100%)}
.sectors-title{color:#fff}
.sectors-copy{left:170px;top:1903px;width:860px;text-align:center;color:#fff;font-size:15px;line-height:26px}
.sector{top:1968px;width:188px;height:176px;background:#fff}
.sector .pic{width:188px;height:127px}
.sector span{display:block;text-align:center;font-family:"Roboto Condensed",sans-serif;font-size:21px;line-height:49px;color:var(--navy)}

/* mission */
.mission{left:0;top:2215px;width:1200px;height:520px;background:linear-gradient(90deg,#eef3fb 0%,#dfe9f6 45%,#b9cde6 100%)}
.mission-building{left:560px;top:2215px;width:640px;height:520px;background:linear-gradient(160deg,#d7e4f3 0%,#a9bfdc 55%,#7f98bd 100%)}
.mission-title{left:78px;top:2278px;font-family:"Roboto Condensed",sans-serif;font-size:46px;color:var(--heading)}
.mission-copy{left:78px;width:520px;font-size:21px;line-height:37px;color:#222}

/* contact */
.block-title{font-family:"Roboto Condensed",sans-serif;font-size:46px;color:var(--heading)}
.field{background:var(--field);border:1px solid var(--field-line);font-size:14px;color:#666;padding:10px 9px}
.submit{left:78px;top:3085px;width:146px;height:46px;line-height:46px;font-size:19px}
.partner-copy{left:644px;top:2830px;width:440px;font-size:15px;line-height:25px}
.partner{font-family:"Roboto Condensed",sans-serif;font-weight:700;font-size:30px;color:var(--navy);display:flex;align-items:center;gap:8px}
.partner i{display:inline-block;width:12px;height:12px;background:var(--accent)}
.read-more{left:641px;top:3085px;width:164px;height:46px;line-height:46px;font-size:19px}

/* footer */
.footer{left:0;top:3215px;width:1200px;height:247px;background:var(--navy-deep);color:#fff}
.foot-nav{left:78px;top:3241px;display:flex;gap:36px;font-size:17px}
.social{top:3241px;display:flex;gap:28px;left:942px}
.social i{display:block;width:18px;height:18px;border-radius:50%;border:2px solid #fff}
.foot-rule{left:78px;top:3290px;width:1044px;height:1px;background:rgba(255,255,255,.25)}
.foot-label{left:78px;top:3310px;font-size:20px}
.foot-item{top:3352px;display:flex;align-items:center;gap:14px;font-size:15px;line-height:22px}
.foot-icon{width:46px;height:46px;border-radius:50%;background:#fff;display:flex;align-items:center;justify-content:center;flex:none}
</style>
</head>
<body>

<!-- hero -->
<div class="abs hero" role="img" aria-label="Glowing world map with network light trails and a laptop outline in blue tones"></div>
<div class="abs header"></div>
<div class="abs brand"><span class="brand-dot"></span>VarloNet</div>
<div class="abs search">Search here...
  <svg width="20" height="20" viewBox="0 0 20 20"><circle cx="8" cy="8" r="6" fill="none" stroke="#333" stroke-width="2.4"/><line x1="12.5" y1="12.5" x2="18" y2="18" stroke="#333" stroke-width="2.6"/></svg>
</div>
<div class="abs phone-top">
  <svg width="20" height="20" viewBox="0 0 24 24"><path d="M6.6 10.8a15 15 0 0 0 6.6 6.6l2.2-2.2a1 1 0 0 1 1-.25 11.4 11.4 0 0 0 3.6.57 1 1 0 0 1 1 1V20a1 1 0 0 1-1 1A17 17 0 0 1 3 4a1 1 0 0 1 1-1h3.5a1 1 0 0 1 1 1c0 1.25.2 2.45.57 3.6a1 1 0 0 1-.25 1z" fill="#1f3566"/></svg>
  +61 3 5550 0142
</div>
<nav class="abs nav">
  <a class="active">Home</a><a>Product &amp; Services</a><a>Sectors</a><a>Support</a><a>Corporate</a><a>Contact</a>
</nav>
<h1 class="abs hero-title" style="font-weight:400">To be a leading international provider of advanced and engineered<br>solutions for mission and business critical network</h1>
<a class="abs btn hero-btn">Contact Us</a>

<!-- welcome -->
<h2 class="abs welcome-title" style="font-weight:400">Welcome to <span class="hl">VarloNet Link Systems</span></h2>
<p class="abs welcome-copy">VarloNet Link Systems is an Australian owned company that provides turnkey communications networks to customers around the world. Founded in 1998, the company has grown to be the leading supplier of communications systems and equipment in its field. Our core business covers the utilities and carrier markets, and have succeeded in expanding our profile into the emergency services sector.</p>

<div class="abs feature-img" style="left:76px;top:1068px;background:linear-gradient(135deg,#c9d3d8,#8e9aa3)" role="img" aria-label="Technician working in an equipment room"></div>
<div class="abs" style="left:303px;top:1060px">
  <div class="feature-title">Technology <span class="hl">&amp; Services</span></div>
  <p class="feature-copy">VarloNet brings together global expertise and the latest technology, helping to meet the growing demands of our customers.</p>
  <div class="more">READ MORE <svg width="14" height="12" viewBox="0 0 14 12"><path d="M1 1l5 5-5 5M7 1l5 5-5 5" fill="none" stroke="#1f3566" stroke-width="2"/></svg></div>
</div>
<div class="abs feature-img" style="left:623px;top:1068px;background:linear-gradient(135deg,#e6ecf2,#a8b8c8)" role="img" aria-label="Team meeting around an office table"></div>
<div class="abs" style="left:850px;top:1060px">
  <div class="feature-title">Operations <span class="hl">Management</span></div>
  <p class="feature-copy">VarloNet operates under an integrated management system covering Quality, Health and Safety, Environment and Security.</p>
  <div class="more">READ MORE <svg width="14" height="12" viewBox="0 0 14 12"><path d="M1 1l5 5-5 5M7 1l5 5-5 5" fill="none" stroke="#1f3566" stroke-width="2"/></svg></div>
</div>

<!-- business -->
<div class="abs business"></div>
<h2 class="abs section-title" style="top:1340px;font-weight:400">Our <span class="hl">Business</span></h2>

<div class="abs service" style="left:71px;top:1415px">
  <svg width="122" height="122" viewBox="0 0 122 122"><circle cx="61" cy="61" r="58" fill="#fff" stroke="var(--ring)" stroke-width="3"/><circle cx="61" cy="61" r="58" fill="none" stroke="var(--accent)" stroke-width="3" stroke-dasharray="120 400" transform="rotate(10 61 61)"/>
  <g fill="none" stroke="#1f3566" stroke-width="3"><rect x="40" y="58" width="42" height="16" rx="2"/><path d="M46 58l8-14h14l8 14"/><circle cx="50" cy="66" r="2"/></g></svg>
  <h3>Supply &amp; Solution<br>Development</h3>
  <p>The Supply &amp; Solutions development team is responsible for the assessment...</p>
</div>
<div class="abs service" style="left:283px;top:1415px">
  <svg width="122" height="122" viewBox="0 0 122 122"><circle cx="61" cy="61" r="58" fill="#fff" stroke="var(--ring)" stroke-width="3"/><circle cx="61" cy="61" r="58" fill="none" stroke="var(--accent)" stroke-width="3" stroke-dasharray="120 400" transform="rotate(10 61 61)"/>
  <g fill="none" stroke="#1f3566" stroke-width="3"><circle cx="61" cy="50" r="4"/><path d="M61 54l-10 26M61 54l10 26M54 70h14M49 40a16 16 0 0 0 0 20M73 40a16 16 0 0 1 0 20M43 34a24 24 0 0 0 0 32M79 34a24 24 0 0 1 0 32"/></g></svg>
  <h3>Rapid Site Solution</h3>
  <p>The Rapid Site Solution(RSS) team provides a unique semi-permanent, self-contained communications hut</p>
</div>
<div class="abs service" style="left:498px;top:1415px">
  <svg width="122" height="122" viewBox="0 0 122 122"><circle cx="61" cy="61" r="58" fill="#fff" stroke="var(--ring)" stroke-width="3"/><circle cx="61" cy="61" r="58" fill="none" stroke="var(--accent)" stroke-width="3" stroke-dasharray="120 400" transform="rotate(10 61 61)"/>
  <g fill="none" stroke="#1f3566" stroke-width="3"><rect x="40" y="40" width="42" height="42" rx="8"/><path d="M48 52h26M48 61h26M48 70h26"/><circle cx="56" cy="52" r="3" fill="#fff"/><circle cx="67" cy="61" r="3" fill="#fff"/><circle cx="54" cy="70" r="3" fill="#fff"/></g></svg>
  <h3>Operational Support<br>Systems</h3>
  <p>The Operational Support Systems (OSS) team is a specialist unit focusing on the development...</p>
</div>
<div class="abs service" style="left:712px;top:1415px">
  <svg width="122" height="122" viewBox="0 0 122 122"><circle cx="61" cy="61" r="58" fill="#fff" stroke="var(--ring)" stroke-width="3"/><circle cx="61" cy="61" r="58" fill="none" stroke="var(--accent)" stroke-width="3" stroke-dasharray="120 400" transform="rotate(10 61 61)"/>
  <g fill="none" stroke="#1f3566" stroke-width="3"><path d="M42 62v-6a19 19 0 0 1 38 0v6"/><rect x="38" y="58" width="8" height="14" rx="3"/><rect x="76" y="58" width="8" height="14" rx="3"/><path d="M80 72c0 8-8 10-16 10"/><circle cx="61" cy="58" r="9"/></g></svg>
  <h3>After Sales Support</h3>
  <p>The After Sales Support team offers flexible multi-technology and multi-vendors support services.</p>
</div>
<div class="abs service" style="left:929px;top:1415px">
  <svg width="122" height="122" viewBox="0 0 122 122"><circle cx="61" cy="61" r="58" fill="#fff" stroke="var(--ring)" stroke-width="3"/><circle cx="61" cy="61" r="58" fill="none" stroke="var(--accent)" stroke-width="3" stroke-dasharray="120 400" transform="rotate(10 61 61)"/>
  <g fill="none" stroke="#1f3566" stroke-width="3"><rect x="38" y="38" width="36" height="26" rx="2"/><path d="M44 46h16M44 54h12"/><circle cx="74" cy="62" r="5"/><path d="M68 84V74a6 6 0 0 1 12 0v10M66 68l-8-6"/></g></svg>
  <h3>Training</h3>
  <p>The Training team provides and delivers an extensive portfolio of technology, product and systems training courses</p>
</div>

<!-- sectors -->
<div class="abs sectors" role="img" aria-label="Deep blue band with faint world map texture"></div>
<h2 class="abs section-title sectors-title" style="top:1832px;font-weight:400">Our Business Sectors</h2>
<p class="abs sectors-copy">VarloNet specialises in design and development of systems and networks that meet the stringent requirements of mission-critical industries.</p>

<div class="abs sector" style="left:78px"><div class="pic" style="background:linear-gradient(180deg,#9ec3e6,#c7c9c4 60%,#8b8c86)" role="img" aria-label="Oil and gas refinery"></div><span>Oil &amp; Gas</span></div>
<div class="abs sector" style="left:293px"><div class="pic" style="background:linear-gradient(180deg,#b8c7d6,#6e6f6a 70%,#3f3f3b)" role="img" aria-label="Electricity substation"></div><span>Electricity Utilities</span></div>
<div class="abs sector" style="left:507px"><div class="pic" style="background:linear-gradient(180deg,#e8b45a,#b9782e 55%,#4a3a2a)" role="img" aria-label="Freight train at sunset"></div><span>Transport</span></div>
<div class="abs sector" style="left:720px"><div class="pic" style="background:linear-gradient(180deg,#8fb4d9,#b08a5c 55%,#6f5638)" role="img" aria-label="Mining haul truck"></div><span>Mining</span></div>
<div class="abs sector" style="left:935px"><div class="pic" style="background:linear-gradient(180deg,#6b9fd3,#a9c8e8)" role="img" aria-label="Telecommunications tower"></div><span>Carrier</span></div>

<!-- mission -->
<div class="abs mission"></div>
<div class="abs mission-building" role="img" aria-label="Modern glass office building"></div>
<h2 class="abs mission-title" style="font-weight:400">Our <span class="hl">Mission</span></h2>
<p class="abs mission-copy" style="top:2357px">To be a leading international provider of advanced and engineered solutions for mission and business critical networks</p>
<p class="abs mission-copy" style="top:2537px">These are delivered through partnership with customers, a highly skilled workforce, excellence in professional services and innovation</p>

<!-- contact -->
<h2 class="abs block-title" style="left:78px;top:2770px;font-weight:400">Get In <span class="hl">Touch With Us</span></h2>
<div class="abs field" style="left:78px;top:2848px;width:227px;height:41px">Enter Name</div>
<div class="abs field" style="left:325px;top:2848px;width:231px;height:41px">Enter Contact No.</div>
<div class="abs field" style="left:78px;top:2910px;width:478px;height:41px">Enter Email id</div>
<div class="abs field" style="left:78px;top:2972px;width:478px;height:93px">Enter Message</div>
<a class="abs btn submit">Submit</a>

<h2 class="abs block-title" style="left:644px;top:2770px;font-weight:400">Business <span class="hl">Partner</span></h2>
<p class="abs partner-copy">VarloNet brings together global expertise and the latest technology, helping to meet the growing demands of our customers.</p>
<div class="abs partner" style="left:640px;top:2922px">Kestrel</div>
<div class="abs partner" style="left:848px;top:2922px"><i></i>Orvane</div>
<div class="abs partner" style="left:1040px;top:2922px">Quorva</div>
<div class="abs partner" style="left:640px;top:3008px">Tidecrest</div>
<div class="abs partner" style="left:792px;top:3008px">Haldorsen</div>
<div class="abs partner" style="left:965px;top:3008px">Pellion</div>
<a class="abs btn read-more">Read More</a>

<!-- footer -->
<div class="abs footer"></div>
<div class="abs foot-nav" style="color:#fff"><span>Home</span><span>Product &amp; Services</span><span>Sectors</span><span>Support</span><span>Corporate</span><span>Contact</span></div>
<div class="abs social" aria-label="Social links"><i></i><i></i><i></i><i></i></div>
<div class="abs foot-rule"></div>
<div class="abs foot-label" style="color:#fff">Contact Us</div>
<div class="abs foot-item" style="left:78px;color:#fff">
  <span class="foot-icon"><svg width="18" height="22" viewBox="0 0 18 22"><path d="M9 1a7 7 0 0 0-7 7c0 5 7 13 7 13s7-8 7-13a7 7 0 0 0-7-7z" fill="#1b2d58"/><circle cx="9" cy="8" r="2.6" fill="#fff"/></svg></span>
  <span>14 Meridian Way<br>Eastmoor Park, Victoria<br>Australia 3099</span>
</div>
<div class="abs foot-item" style="left:348px;color:#fff;font-weight:700">
  <span class="foot-icon"><svg width="20" height="20" viewBox="0 0 24 24"><path d="M6.6 10.8a15 15 0 0 0 6.6 6.6l2.2-2.2a1 1 0 0 1 1-.25 11.4 11.4 0 0 0 3.6.57 1 1 0 0 1 1 1V20a1 1 0 0 1-1 1A17 17 0 0 1 3 4a1 1 0 0 1 1-1h3.5a1 1 0 0 1 1 1c0 1.25.2 2.45.57 3.6a1 1 0 0 1-.25 1z" fill="#1b2d58"/></svg></span>
  <span>+61 3 5550 0142</span>
</div>
<div class="abs foot-item" style="left:618px;color:#fff">
  <span class="foot-icon"><svg width="22" height="20" viewBox="0 0 22 20"><rect x="5" y="1" width="12" height="6" fill="none" stroke="#1b2d58" stroke-width="2"/><rect x="1" y="7" width="20" height="10" rx="2" fill="#1b2d58"/><rect x="5" y="13" width="12" height="6" fill="#fff" stroke="#1b2d58" stroke-width="2"/></svg></span>
  <span>+61 3 5550 0198</span>
</div>
<div class="abs foot-item" style="left:892px;color:#fff;font-size:14px">
  <span>© VarloNet Link Systems<br>- 2016, All Rights Reserved.</span>
</div>

</body>
</html>
```